Amber Burrows Business Card Design

Amber Burrows - Gathering Gentle Meadow Corners

Amber Burrows is a company that focuses on promoting the design, construction, consultation and support of natural, creative and organic play spaces for Early Childhood and learning environments.

We need a professional Business Card designed that is unique modern and creative. The Philosophy of the company is nostalgic so the business and will need to reflect this but also reflect that our ideas are modern and cutting edge.

The business card will need to be a talking point, by either having a unique size, quality and/or placement of logo or other quality.

I am more interested in using natural recycled paper, as this would reflect the philosophy of the company, but I open to seeing colour used creatively.
Updates

Hi Designers, Apologies, Could you please add www.amberburrows.com.au to the business card. Thanks very much.

Hi All, Thank you all for your submission thus far. Please note the fonts for used in the logo are: Ostrich Sans Black and Archer Semi Bold. If these could be considered for contact details, my name etc. Also please show the design on a recycled brown card if possible as this will be the type of card I will use when printing. Thanks so much.

Target Market(s)

Child Care Providers, Play Industry Professionals

Industry/Entity Type

Business

Contact Information for Business Card

Amber Burrows
Gathering Gentle Meadow Corners
Marguerite Holloway
0419 862 503
marguerite@amberburrows.com.au

Font styles to use
Sans Serif

Requirements
Must have
• The Logo and the Details plus the below phrase
• Amber Burrows - Gathering Gentle Meadow Corners
Nice to have
• A bit of colour, but not too much colour.
Should not have
• Not to have a white background, recycled brown card only

```html
<!DOCTYPE html>
<html lang="en">
<head>
<meta charset="utf-8">
<title>Amber Burrows Business Card Design</title>
<link rel="stylesheet" href="https://fonts.googleapis.com/css2?family=Open+Sans:wght@400;600;700;800&family=Arvo:wght@400;700&display=swap">
<style>
  :root {
    --canvas: #2b2b2b;
    --card-black: #050505;
    --sky: #29abe2;
    --sky-deep: #1f9fd6;
    --paper: #ffffff;
    --ink: #111111;
    --rule: #161616;
  }
  * { box-sizing: border-box; margin: 0; padding: 0; }
  html, body {
    width: 1200px;
    height: 900px;
    overflow: hidden;
    background: var(--canvas);
  }
  .canvas {
    position: relative;
    width: 1200px;
    height: 900px;
  }
  .card {
    position: absolute;
    width: 640px;
    height: 366px;
    border-radius: 24px;
    overflow: hidden;
  }

  /* Front */
  .card-front {
    left: 110px;
    top: 70px;
    background: var(--card-black);
    display: flex;
    align-items: center;
    justify-content: center;
  }
  .brand {
    display: flex;
    flex-direction: column;
    align-items: center;
    gap: 12px;
  }
  .brand-row {
    display: flex;
    align-items: center;
    gap: 14px;
  }
  .brand-dot {
    width: 22px;
    height: 22px;
    border-radius: 50%;
    background: currentColor;
  }
  .brand-name {
    font-family: "Open Sans", sans-serif;
    font-weight: 800;
    font-size: 44px;
    letter-spacing: 1px;
    text-transform: uppercase;
    line-height: 1;
  }
  .brand-tagline {
    font-family: "Arvo", serif;
    font-weight: 400;
    font-size: 15px;
    letter-spacing: 1.5px;
    text-transform: uppercase;
    text-align: center;
    line-height: 1.25;
  }
  .card-front .brand { color: var(--paper); }

  /* Back */
  .card-back {
    left: 450px;
    top: 464px;
    background: var(--paper);
  }
  .back-band {
    position: absolute;
    left: 0; top: 0;
    width: 100%;
    height: 238px;
    background: var(--sky);
    border-bottom: 4px solid var(--rule);
  }
  .card-back .brand {
    position: absolute;
    left: 40px;
    top: 52px;
    align-items: flex-start;
    color: var(--ink);
    gap: 8px;
  }
  .card-back .brand-name { font-size: 32px; }
  .card-back .brand-dot { width: 16px; height: 16px; }
  .card-back .brand-tagline { font-size: 12px; text-align: left; }
  .holder-name {
    position: absolute;
    left: 40px;
    top: 192px;
    font-family: "Open Sans", sans-serif;
    font-weight: 800;
    font-size: 25px;
    letter-spacing: 1px;
    color: var(--ink);
    text-transform: uppercase;
  }
  .contact-list {
    position: absolute;
    left: 40px;
    top: 264px;
    list-style: none;
    font-family: "Open Sans", sans-serif;
    font-weight: 600;
    font-size: 17px;
    color: var(--ink);
  }
  .contact-list li {
    display: flex;
    align-items: center;
    gap: 12px;
    margin-bottom: 10px;
  }
  .contact-icon {
    width: 16px;
    height: 16px;
    flex: none;
  }
</style>
</head>
<body>
<main class="canvas">

  <section class="card card-front" aria-label="Business card front">
    <div class="brand">
      <div class="brand-row">
        <span class="brand-dot"></span>
        <span class="brand-name">Amber Burrows</span>
      </div>
      <p class="brand-tagline">Gathering<br>Gentle Meadow Corners</p>
    </div>
  </section>

  <section class="card card-back" aria-label="Business card back">
    <div class="back-band"></div>
    <div class="brand">
      <div class="brand-row">
        <span class="brand-dot"></span>
        <span class="brand-name">Amber Burrows</span>
      </div>
      <p class="brand-tagline">Gathering Gentle Meadow Corners</p>
    </div>
    <h1 class="holder-name">Marguerite Holloway</h1>
    <ul class="contact-list">
      <li>
        <svg class="contact-icon" viewBox="0 0 24 24" aria-hidden="true">
          <path fill="var(--sky-deep)" d="M6.6 10.8a15.1 15.1 0 0 0 6.6 6.6l2.2-2.2a1 1 0 0 1 1-.25 11.4 11.4 0 0 0 3.6.57 1 1 0 0 1 1 1V20a1 1 0 0 1-1 1A17 17 0 0 1 3 4a1 1 0 0 1 1-1h3.5a1 1 0 0 1 1 1c0 1.25.2 2.45.57 3.57a1 1 0 0 1-.25 1z"/>
        </svg>
        <span>0419 862 503</span>
      </li>
      <li>
        <svg class="contact-icon" viewBox="0 0 24 24" aria-hidden="true">
          <rect x="2.5" y="5" width="19" height="14" rx="2" fill="none" stroke="var(--sky-deep)" stroke-width="2.2"/>
          <path d="M3 6l9 7 9-7" fill="none" stroke="var(--sky-deep)" stroke-width="2.2"/>
        </svg>
        <span>marguerite@amberburrows.com.au</span>
      </li>
    </ul>
  </section>

</main>
</body>
</html>
```